I need a business card design for a new company that will be doing consulting work around issues of cultural competency, and diversity and inclusion. I would like the design to be crisp and clear with bold but conservative colors and incorporate shades of blue

Target Market(s)

Small businesses, schools, non-profits

Industry/Entity Type

Consulting

Font styles to use
Serif
Sans Serif

Colors
0c5ba6
6b449b
3276b5
0292cd

Requirements
Must have
• A Morrow Venture (name of company)
• Lemlem Tavish
• CEO
• lemlem@amorrowventure.com
• (215)483-2756

```html
<!DOCTYPE html>
<html lang="en">
<head>
<meta charset="utf-8">
<title>Lemlem Tavish – Business Card</title>
<link rel="stylesheet" href="https://fonts.googleapis.com/css2?family=Jost:wght@300;800&family=Open+Sans:wght@400&display=swap">
<style>
  :root {
    --navy: #0c5ba6;
    --mid-blue: #3276b5;
    --sky: #0292cd;
    --sky-light: #4bb0dc;
    --soft-blue: #6fa6d8;
    --paper: #ffffff;
  }
  html, body {
    margin: 0;
    padding: 0;
    overflow: hidden;
    background: var(--paper);
  }
  .card {
    position: relative;
    width: 1200px;
    height: 514px;
    background: var(--paper);
    overflow: hidden;
  }
  .waves {
    position: absolute;
    inset: 0;
    width: 1200px;
    height: 514px;
  }
  .identity {
    position: absolute;
    left: 160px;
    top: 62px;
    margin: 0;
  }
  .person-name {
    margin: 0;
    font-family: "Jost", sans-serif;
    font-size: 80px;
    line-height: 1;
    letter-spacing: 2px;
    text-transform: uppercase;
    color: var(--navy);
  }
  .first-name { font-weight: 800; margin-right: 22px; }
  .last-name { font-weight: 300; }
  .job-title {
    margin: 2px 0 0 2px;
    font-family: "Open Sans", sans-serif;
    font-weight: 400;
    font-size: 40px;
    line-height: 1.1;
    color: var(--soft-blue);
  }
  .contact-list {
    position: absolute;
    left: 164px;
    top: 221px;
    height: 102px;
    margin: 0;
    padding: 0 0 0 14px;
    list-style: none;
    border-left: 1.5px solid var(--mid-blue);
    font-family: "Open Sans", sans-serif;
    font-size: 24px;
    color: var(--mid-blue);
  }
  .contact-item {
    display: flex;
    align-items: center;
    height: 48px;
  }
  .contact-icon {
    width: 40px;
    height: 40px;
    margin-right: 18px;
    flex: none;
  }
</style>
</head>
<body>
<div class="card">
  <svg class="waves" viewBox="0 0 1400 600" preserveAspectRatio="none" aria-hidden="true">
    <defs>
      <linearGradient id="sky-wave" x1="0" y1="0" x2="1" y2="0">
        <stop offset="0" stop-color="#0f8fcf"/>
        <stop offset="0.4" stop-color="#4bb0dc"/>
        <stop offset="0.75" stop-color="#0292cd"/>
        <stop offset="1" stop-color="#0a88c8"/>
      </linearGradient>
      <linearGradient id="navy-wave" x1="0.6" y1="0.3" x2="1" y2="1">
        <stop offset="0" stop-color="#0c5ba6"/>
        <stop offset="0.8" stop-color="#1660aa"/>
        <stop offset="1" stop-color="#3276b5"/>
      </linearGradient>
    </defs>
    <path class="wave-navy" fill="url(#navy-wave)"
      d="M0,460 C200,530 430,585 650,548 C900,500 1150,355 1400,350 L1400,600 L0,600 Z"/>
    <path class="wave-sky" fill="url(#sky-wave)" stroke="#ffffff" stroke-width="6"
      d="M95,478 C350,505 620,470 860,395 C1010,350 1100,310 1230,310 C1300,310 1360,322 1398,333
         C1260,338 1150,352 1040,392 C890,448 760,512 600,536 C420,560 250,525 95,478 Z"/>
  </svg>

  <header class="identity">
    <h1 class="person-name"><span class="first-name">Lemlem</span><span class="last-name">Tavish</span></h1>
    <p class="job-title">CEO</p>
  </header>

  <ul class="contact-list">
    <li class="contact-item">
      <svg class="contact-icon" viewBox="0 0 40 40" fill="none" stroke="#3276b5" stroke-width="1.5" aria-hidden="true">
        <circle cx="20" cy="20" r="17"/>
        <ellipse cx="20" cy="20" rx="7.5" ry="17"/>
        <line x1="20" y1="3" x2="20" y2="37"/>
        <line x1="3" y1="20" x2="37" y2="20"/>
        <path d="M6 11 H34 M6 29 H34"/>
      </svg>
      <span class="contact-email">lemlem@amorrowventure.com</span>
    </li>
    <li class="contact-item">
      <svg class="contact-icon" viewBox="0 0 40 40" fill="none" stroke="#3276b5" stroke-width="1.5" stroke-linejoin="round" aria-hidden="true">
        <path d="M9 4 L15 12 L12 16 C14 22 18 26 24 29 L28 26 L36 32 L32 37 C20 36 5 22 4 8 Z"/>
        <path d="M22 9 C27 10 30 13 31 18 M22 4 C30 5 35 10 36 18"/>
      </svg>
      <span class="contact-phone">(215)483-2756</span>
    </li>
  </ul>
</div>
</body>
</html>
```